New Website design for VelvetCrate.com - A Monthly Subscription Sexy Lingerie Biz

Look at these sites: https://www.quillrazorguild.com; http://www.parcelwardrobe.com; http://www.tinyfernpack.com; https://www.ochreladle.com; https://thegoldenradish.com; http://www.petalwickcrate.com; https://wagtote.com; https://www.marlowehush.com/coral

Industry/Entity Type

Lingerie

Coding

Coded - Design and coding required

Number of Pages Required

1 page

```html
<!DOCTYPE html>
<html lang="en">
<head>
<meta charset="utf-8">
<title>VelvetCrate – Monthly Lingerie Subscription</title>
<link href="https://fonts.googleapis.com/css2?family=Raleway:wght@400;500;700&family=Roboto:ital,wght@0,400;0,500;1,400&family=Roboto+Condensed:wght@400;700&display=swap" rel="stylesheet">
<style>
:root{
  --pink:#ef5a8b;
  --pink-soft:rgba(239,90,139,.55);
  --ink:#2b2b2b;
  --muted:#666;
  --bar:#222;
  --cart:#3a3a3a;
  --footer:#333;
  --base:#0f0f0f;
  --line:#e2e2e2;
}
*{box-sizing:border-box;margin:0;padding:0}
html,body{width:1200px;height:2582px;overflow:hidden}
body{position:relative;font-family:'Roboto',sans-serif;color:var(--ink);background:#fff}
.abs{position:absolute}

/* top bar */
.topbar{position:absolute;left:0;top:0;width:1200px;height:57px;background:var(--bar);color:#fff;font-size:12px}
.topbar .lang{left:92px;top:20px}
.topbar .phone{left:234px;top:20px;display:flex;gap:8px;align-items:center}
.topbar .links{left:592px;top:20px;display:flex;gap:14px}
.topbar .cart{left:885px;top:0;width:90px;height:57px;background:var(--cart);display:flex;align-items:center;justify-content:center;gap:8px;font-size:17px}
.topbar .social{left:998px;top:18px;display:flex;gap:9px}
.topbar .social span{width:20px;height:20px;background:#fff;border-radius:3px}

/* header */
.header{position:absolute;left:0;top:57px;width:1200px;height:106px;background:#fff;border-bottom:1px solid var(--line)}
.logo{font-family:'Raleway',sans-serif;font-weight:700;color:var(--pink);font-size:36px}
.header .logo{left:90px;top:32px}
.nav{font-size:14.5px}
.nav a{position:absolute;white-space:nowrap;color:#333;text-decoration:none}

/* hero */
.hero{position:absolute;left:0;top:163px;width:1200px;height:567px;background:linear-gradient(120deg,#cdb4a2 0%,#e9d9cb 40%,#efe4d8 65%,#d6c2b2 100%)}
.hero .caption{left:90px;top:410px;width:547px;height:128px;background:var(--pink-soft);padding:20px 0 0 28px;color:#fff}
.caption h1{font-family:'Roboto Condensed',sans-serif;font-weight:400;font-size:40px;letter-spacing:-.4px;line-height:46px;white-space:nowrap}
.caption p{font-size:24px;line-height:30px;margin-top:2px;white-space:nowrap}
.hero .arrows{left:1043px;top:493px;display:flex;gap:2px}
.arrows span{width:32px;height:41px;background:rgba(60,60,60,.75);display:flex;align-items:center;justify-content:center}

/* section titles */
.title{position:absolute;left:0;width:1200px;text-align:center;font-family:'Raleway',sans-serif;font-size:26px;font-weight:500}

/* how it works */
.how .title{top:773px;color:var(--pink)}
.step{position:absolute;width:320px;text-align:center}
.step .ring{width:120px;height:120px;margin:0 auto;border-radius:50%;border:4px solid #eee;box-shadow:0 0 0 1px #ddd;display:flex;align-items:center;justify-content:center;background:#fff}
.step h3{font-family:'Raleway',sans-serif;font-weight:500;font-size:18px;margin-top:32px;color:#333}
.step p{font-size:11.5px;line-height:19px;color:#555;margin:12px auto 0;width:270px}
.flow{position:absolute;top:882px}

/* collection */
.collection{position:absolute;left:0;top:1116px;width:1200px;height:542px;background:linear-gradient(180deg,#3e3e3e,#2e2e2e)}
.collection .title{top:45px;color:#fff}
.card{position:absolute;top:124px;width:233px;height:360px;background:#fff}
.card .photo{height:239px;background:linear-gradient(180deg,#e6dcd6,#c9b1a6)}
.card .name{height:34px;background:#ececec;text-align:center;line-height:34px;font-size:16px;color:#333}
.card .price{height:45px;text-align:center;line-height:45px;font-size:17px}
.price s{color:#999;font-size:13px;margin-right:8px}
.card .actions{display:flex;height:42px;border-top:1px solid #e5e5e5}
.actions span{flex:1;display:flex;align-items:center;justify-content:center;border-left:1px solid #e5e5e5}
.actions span:first-child{border-left:none}
.actions .on{background:var(--pink)}
.collection .more{left:1036px;top:506px;color:#fff;font-size:15px;text-decoration:underline}

/* reviews */
.reviews .title{top:1712px;color:#222}
.reviews .title em{font-style:normal;color:var(--pink)}
.review{position:absolute;top:1790px}
.avatar{position:absolute;width:114px;height:114px;border-radius:50%;border:4px solid #ddd;background:linear-gradient(160deg,#caa28a,#8e6a56)}
.review .body{position:absolute;left:134px;top:0;width:320px}
.stars{color:#f2c218;font-size:20px;letter-spacing:1px}
.stars .off{color:#ddd}
.review q{display:block;font-style:italic;font-size:12px;line-height:22px;color:#333;margin-top:2px;quotes:none}
.review .who{color:var(--pink);font-size:11px;margin-top:4px}
.review .role{font-size:11px;color:#333;margin-top:4px}

/* newsletter */
.newsletter{position:absolute;left:0;top:1971px;width:1200px;height:154px;background:var(--pink)}
.newsletter h2{position:absolute;left:114px;top:64px;font-family:'Raleway',sans-serif;font-weight:500;font-size:26px;color:#fff}
.newsletter .field{position:absolute;left:544px;top:52px;width:346px;height:60px;background:#fff;padding:0 18px;line-height:60px;color:#666;font-size:15px}
.newsletter .btn{position:absolute;left:907px;top:52px;width:166px;height:62px;background:linear-gradient(180deg,#555,#111);color:#fff;text-align:center;line-height:62px;font-size:16px;font-weight:500}

/* partners */
.partners{position:absolute;left:0;top:2125px;width:1200px;height:148px}
.partners span{position:absolute;top:62px;font-family:'Raleway',sans-serif;font-weight:700;font-size:22px;color:#333;display:flex;align-items:center;gap:8px}
.partners i{width:22px;height:22px;border-radius:50%;background:#555;display:block}

/* footer */
.footer{position:absolute;left:0;top:2273px;width:1200px;height:223px;background:var(--footer);color:#fff}
.fcol{position:absolute;top:46px;font-size:11px}
.fcol h4{font-size:14px;font-weight:500;line-height:16px;margin-bottom:18px}
.fcol ul{list-style:none;line-height:24.5px}
.fcol li::before{content:"▸ ";font-size:9px}
.fcol .quote{font-style:italic;line-height:17px;width:236px;font-size:10.5px}
.fcol .client{font-size:10.5px;line-height:17px;margin-top:4px}
.fcol p{line-height:21px}
.fsocial{display:flex;gap:15px;margin-top:14px}
.fsocial span{width:32px;height:32px;border-radius:50%;background:var(--pink);border:2px solid #fff}

/* base */
.base{position:absolute;left:0;top:2496px;width:1200px;height:86px;background:var(--base);color:#fff}
.base .logo{position:absolute;left:90px;top:26px;font-size:24px}
.base .copy{position:absolute;left:909px;top:36px;font-size:12px}
</style>
</head>
<body>

<div class="topbar">
  <div class="abs lang">Language: English ˅</div>
  <div class="abs phone">
    <svg width="15" height="15" viewBox="0 0 16 16"><circle cx="8" cy="8" r="7" fill="none" stroke="#fff" stroke-width="1.4"/><path d="M5.5 4.5l1.4 1.6-.8 1c.6 1.2 1.4 2 2.6 2.6l1-.8 1.6 1.4-.9 1.2C7.6 11.4 4.6 8.4 4.4 5.3z" fill="#fff"/></svg>
    1-800-55501234
  </div>
  <div class="abs links"><span>Account</span><span>|</span><span>Wishlist</span><span>|</span><span>Checkout</span><span>|</span><span>Log In</span></div>
  <div class="abs cart">
    <svg width="20" height="17" viewBox="0 0 20 17"><path d="M1 1h3l2.5 10h10l2-7H5.5" fill="none" stroke="#fff" stroke-width="2"/><circle cx="8" cy="14.5" r="1.8" fill="#fff"/><circle cx="15" cy="14.5" r="1.8" fill="#fff"/></svg>: 0
  </div>
  <div class="abs social"><span></span><span></span><span></span><span></span></div>
</div>

<header class="header">
  <div class="abs logo">VelvetCrate</div>
  <nav class="abs nav" style="left:0;top:47px;width:1200px">
    <a style="left:442px">SUBSCRIBE</a>
    <a style="left:563px">WHAT'S INSIDE</a>
    <a style="left:708px">SHOP</a>
    <a style="left:789px">BOX RESOURCES</a>
    <a style="left:947px">ABOUT</a>
    <a style="left:1035px">CONTACTS</a>
  </nav>
</header>

<section class="hero" role="img" aria-label="Model in black lace lingerie reclining on cream bedding">
  <div class="abs caption">
    <h1>SUBSCRIPTION SEXY LINGERIE BIZ</h1>
    <p>Neque porro quisquam est qui dolorem</p>
  </div>
  <div class="abs arrows">
    <span><svg width="12" height="20"><path d="M10 2L3 10l7 8" fill="none" stroke="#fff" stroke-width="1.6"/></svg></span>
    <span><svg width="12" height="20"><path d="M2 2l7 8-7 8" fill="none" stroke="#fff" stroke-width="1.6"/></svg></span>
  </div>
</section>

<section class="how">
  <h2 class="title">HOW IT WORKS</h2>
  <div class="step" style="left:72px;top:835px">
    <div class="ring"><svg width="54" height="34" viewBox="0 0 54 34"><path d="M2 3h50v8c-10 2-17 10-19 21H21C19 21 12 13 2 11z" fill="var(--pink)"/><path d="M2 7h50" stroke="#fff" stroke-width="1.5"/></svg></div>
    <h3>1 SING UP</h3>
    <p>Lorem ipsum dolor sit amet, consectetur adipising elit, sed do eiusmod tempor iunt ut labore et dolore magna aliqua. eiusmod</p>
  </div>
  <svg class="flow" style="left:404px" width="38" height="30" viewBox="0 0 38 30"><path d="M3 27c0-12 8-17 20-17V3l13 11-13 11v-7C13 18 7 21 3 27z" fill="#555"/></svg>
  <div class="step" style="left:440px;top:835px">
    <div class="ring"><svg width="38" height="56" viewBox="0 0 38 56"><path d="M8 2h4c0 8 3 12 7 12s7-4 7-12h4v14c5 4 7 10 6 16l-2 22H4L2 32c-1-6 1-12 6-16z" fill="var(--pink)"/></svg></div>
    <h3>2 WHAT'S YOUR SIZE?</h3>
    <p>Lorem ipsum dolor sit amet, consectetur adipising elit, sed do eiusmod tempor iunt ut labore et dolore magna aliqua. eiusmod</p>
  </div>
  <svg class="flow" style="left:776px" width="38" height="30" viewBox="0 0 38 30"><path d="M3 27c0-12 8-17 20-17V3l13 11-13 11v-7C13 18 7 21 3 27z" fill="#555"/></svg>
  <div class="step" style="left:809px;top:835px">
    <div class="ring"><svg width="60" height="46" viewBox="0 0 60 46"><path d="M14 2l2 18M46 2l-2 18" stroke="var(--pink)" stroke-width="3"/><path d="M2 40c2-14 10-22 20-22 5 0 8 6 8 14 0-8 3-14 8-14 10 0 18 8 20 22-10 4-20 2-28-6-8 8-18 10-28 6z" fill="var(--pink)"/></svg></div>
    <h3>3 ENJOY!</h3>
    <p>Lorem ipsum dolor sit amet, consectetur adipising elit, sed do eiusmod tempor iunt ut labore et dolore magna aliqua. eiusmod</p>
  </div>
</section>

<section class="collection">
  <h2 class="title">OUR COLLECTION</h2>

  <article class="card" style="left:91px">
    <div class="photo" role="img" aria-label="Model wearing a black balconette lingerie set"></div>
    <div class="name">Lorem ipsum dolor</div>
    <div class="price"><s>$160.00</s><span style="color:var(--pink)">$150.00</span></div>
    <div class="actions">
      <span class="on"><svg width="18" height="16"><path d="M1 2h3l2 8h9l2-6H5" fill="none" stroke="#fff" stroke-width="1.8"/><circle cx="7" cy="13.5" r="1.5" fill="#fff"/><circle cx="14" cy="13.5" r="1.5" fill="#fff"/></svg></span>
      <span><svg width="16" height="14"><path d="M8 13L2 7a3.3 3.3 0 0 1 6-4 3.3 3.3 0 0 1 6 4z" fill="#888"/></svg></span>
      <span><svg width="16" height="14"><path d="M1 4h11l-3-3M15 10H4l3 3" fill="none" stroke="#888" stroke-width="1.8"/></svg></span>
      <span><svg width="16" height="16"><circle cx="8" cy="8" r="6.5" fill="none" stroke="#888" stroke-width="1.5"/><path d="M8 7v5" stroke="#888" stroke-width="1.8"/><circle cx="8" cy="4.6" r="1" fill="#888"/></svg></span>
    </div>
  </article>

  <article class="card" style="left:355px">
    <div class="photo" role="img" aria-label="Model wearing a white lace lingerie set" style="background:linear-gradient(180deg,#cfe3ee,#e9e2da)"></div>
    <div class="name">Lorem ipsum dolor</div>
    <div class="price"><s>$160.00</s>$150.00</div>
    <div class="actions">
      <span><svg width="18" height="16"><path d="M1 2h3l2 8h9l2-6H5" fill="none" stroke="#888" stroke-width="1.8"/><circle cx="7" cy="13.5" r="1.5" fill="#888"/><circle cx="14" cy="13.5" r="1.5" fill="#888"/></svg></span>
      <span><svg width="16" height="14"><path d="M8 13L2 7a3.3 3.3 0 0 1 6-4 3.3 3.3 0 0 1 6 4z" fill="#888"/></svg></span>
      <span><svg width="16" height="14"><path d="M1 4h11l-3-3M15 10H4l3 3" fill="none" stroke="#888" stroke-width="1.8"/></svg></span>
      <span><svg width="16" height="16"><circle cx="8" cy="8" r="6.5" fill="none" stroke="#888" stroke-width="1.5"/><path d="M8 7v5" stroke="#888" stroke-width="1.8"/><circle cx="8" cy="4.6" r="1" fill="#888"/></svg></span>
    </div>
  </article>

  <article class="card" style="left:620px">
    <div class="photo" role="img" aria-label="Model wearing a purple lace lingerie set" style="background:linear-gradient(180deg,#f2eeec,#d8c4c4)"></div>
    <div class="name">Lorem ipsum dolor</div>
    <div class="price"><s>$160.00</s>$150.00</div>
    <div class="actions">
      <span><svg width="18" height="16"><path d="M1 2h3l2 8h9l2-6H5" fill="none" stroke="#888" stroke-width="1.8"/><circle cx="7" cy="13.5" r="1.5" fill="#888"/><circle cx="14" cy="13.5" r="1.5" fill="#888"/></svg></span>
      <span><svg width="16" height="14"><path d="M8 13L2 7a3.3 3.3 0 0 1 6-4 3.3 3.3 0 0 1 6 4z" fill="#888"/></svg></span>
      <span><svg width="16" height="14"><path d="M1 4h11l-3-3M15 10H4l3 3" fill="none" stroke="#888" stroke-width="1.8"/></svg></span>
      <span><svg width="16" height="16"><circle cx="8" cy="8" r="6.5" fill="none" stroke="#888" stroke-width="1.5"/><path d="M8 7v5" stroke="#888" stroke-width="1.8"/><circle cx="8" cy="4.6" r="1" fill="#888"/></svg></span>
    </div>
  </article>

  <article class="card" style="left:883px">
    <div class="photo" role="img" aria-label="Model wearing a sheer black lingerie set" style="background:linear-gradient(180deg,#f3efec,#d9c2b4)"></div>
    <div class="name">Lorem ipsum dolor</div>
    <div class="price"><s>$160.00</s>$150.00</div>
    <div class="actions">
      <span><svg width="18" height="16"><path d="M1 2h3l2 8h9l2-6H5" fill="none" stroke="#888" stroke-width="1.8"/><circle cx="7" cy="13.5" r="1.5" fill="#888"/><circle cx="14" cy="13.5" r="1.5" fill="#888"/></svg></span>
      <span><svg width="16" height="14"><path d="M8 13L2 7a3.3 3.3 0 0 1 6-4 3.3 3.3 0 0 1 6 4z" fill="#888"/></svg></span>
      <span><svg width="16" height="14"><path d="M1 4h11l-3-3M15 10H4l3 3" fill="none" stroke="#888" stroke-width="1.8"/></svg></span>
      <span><svg width="16" height="16"><circle cx="8" cy="8" r="6.5" fill="none" stroke="#888" stroke-width="1.5"/><path d="M8 7v5" stroke="#888" stroke-width="1.8"/><circle cx="8" cy="4.6" r="1" fill="#888"/></svg></span>
    </div>
  </article>

  <a class="abs more">View More</a>
</section>

<section class="reviews">
  <h2 class="title">PEOPLE <em>REVIEW</em></h2>
  <div class="review" style="left:115px">
    <div class="avatar" role="img" aria-label="Portrait of reviewer Mara Lindqvist" style="top:0;left:0"></div>
    <div class="body">
      <div class="stars">★★★<span style="opacity:.7">★</span><span class="off">★</span></div>
      <q>Lorem Ipsum has been the industry's standard dummy text ever since the 1500s, when an unknown printer took a galley of type and scrambled it to make</q>
      <div class="who">Mara Lindqvist</div>
      <div class="role">Neque porro quisquam est</div>
    </div>
  </div>
  <div class="review" style="left:666px">
    <div class="avatar" role="img" aria-label="Portrait of reviewer Tomas Reyes" style="top:0;left:0;background:linear-gradient(160deg,#7b5a48,#3d2a22)"></div>
    <div class="body">
      <div class="stars">★★★<span style="opacity:.7">★</span><span class="off">★</span></div>
      <q>Lorem Ipsum has been the industry's standard dummy text ever since the 1500s, when an unknown printer took a galley of type and scrambled it to make</q>
      <div class="who">Tomas Reyes</div>
      <div class="role">Neque porro quisquam est</div>
    </div>
  </div>
</section>

<section class="newsletter">
  <h2>SUBSCRIBE FOR NEWS LETTERS</h2>
  <div class="field">Enter your email....</div>
  <div class="btn">SUBSCRIBE</div>
</section>

<section class="partners">
  <span style="left:117px"><i></i>Pagecraft</span>
  <span style="left:322px"><i></i>Siteforge</span>
  <span style="left:527px"><i></i>Cartwell</span>
  <span style="left:732px"><i></i>Nodeleaf</span>
  <span style="left:937px"><i></i>Scriptly</span>
</section>

<footer class="footer">
  <div class="fcol" style="left:98px">
    <h4>LINKS</h4>
    <ul><li>Who we are</li><li>How we work</li><li>services</li><li>products</li><li>Blog</li></ul>
  </div>
  <div class="fcol" style="left:305px">
    <h4>CLIENT'S TESTIMONIALS</h4>
    <div class="quote">" Lorem Ipsum has been the industry's standard dummy text ever since the 1500s, when an unknown printer took a galley of type and scrambled it to make a type specimen book. It has survived not only five centuries. "</div>
    <div class="client">Client name, City</div>
  </div>
  <div class="fcol" style="left:659px">
    <h4>GET IN TOUCH</h4>
    <p>Address : 1420 Harbor Lane,<br>Fairview, NJ</p>
    <p style="margin-top:12px">Phone : 201 555 0187</p>
    <p style="margin-top:13px">Email : info@velvetcrate.com</p>
  </div>
  <div class="fcol" style="left:911px">
    <h4>FOLLOW US</h4>
    <p style="font-size:12px">Connect with our social network</p>
    <div class="fsocial"><span></span><span></span><span></span></div>
  </div>
</footer>

<div class="base">
  <div class="logo">VelvetCrate</div>
  <div class="copy">Copyright © 2016. All Rights Reserved</div>
</div>

</body>
</html>
```